Flyer-Design für Infoblatt artgerechte Haltung Meerschweinchen
Zielgruppe
Pfotenkorb-Laden bietet Futter und Zubehör für Meerschweinchen, Kaninchen und andere Nager. Gerne möchte ich auch ein Infoblatt für artgerechte Meerschweinchen anbieten
Aufgabenstellung
Text muss so wie im PDF (InfoblattMeerschweinchen) vorhanden sein

```html
<!DOCTYPE html>
<html lang="de">
<head>
<meta charset="utf-8">
<title>Kleines Meerschweinchen – Infoblatt</title>
<link href="https://fonts.googleapis.com/css2?family=Comic+Neue:ital,wght@0,700;1,700&family=Roboto+Condensed:wght@400;700&display=swap" rel="stylesheet">
<style>
:root{
  --green-light:#b8cb4c;
  --green-dark:#6c7b24;
  --olive-text:#6c7b24;
  --ink:#262626;
  --paper:#ffffff;
  --photo-fur-1:#c9955a;
  --photo-fur-2:#6e4a2a;
  --photo-green-1:#3d4a25;
  --photo-green-2:#8a9a55;
}
*{box-sizing:border-box;margin:0;padding:0}
html,body{width:969px;height:1200px;overflow:hidden;background:var(--paper)}
body{position:relative;font-family:'Roboto Condensed','Arial Narrow',sans-serif;color:var(--ink)}

.sheet{position:absolute;background:var(--paper);box-shadow:0 1px 4px rgba(0,0,0,.28);overflow:hidden}
.band-top{position:absolute;left:0;right:0;top:0;height:5px;background:var(--green-light)}
.band-bottom{position:absolute;left:0;right:0;bottom:0;height:5px;background:var(--green-light)}

.heading{font-family:'Comic Neue',cursive;font-weight:700;color:var(--olive-text);line-height:1.05}
.copy{font-size:5.6px;line-height:9.75px;text-align:justify;hyphens:auto}

.photo{position:absolute}
.wrap-r{float:right;clear:right}
.wrap-l{float:left;clear:left}
.hold-r{float:right;width:0}
.hold-l{float:left;width:0}

.info-circle{position:absolute;border-radius:50%;background:var(--green-dark);color:#fff;text-align:center}
.info-circle .bulb{position:absolute;left:50%;transform:translateX(-50%)}
.info-circle .label{position:absolute;left:50%;background:var(--green-light);color:#fff;font-weight:700;font-size:8.5px;letter-spacing:.2px;padding:1px 9px;white-space:nowrap;transform:translateX(-50%) rotate(-3deg)}
.info-circle .text{position:absolute;left:9px;right:9px;font-size:5.5px;line-height:8.9px}
.info-circle .text b{color:var(--green-light);font-weight:400}

.tag-banner{position:absolute;background:var(--green-light);color:#fff;font-family:'Comic Neue',cursive;font-weight:700;text-align:center;transform:rotate(-6deg)}

.cover{left:110px;top:62px;width:277px;height:504px}
.cover .brand{position:absolute;left:0;right:0;top:62px;text-align:center}
.cover .brand-mark{display:block;width:30px;height:30px;border-radius:50%;background:var(--green-light);margin:0 auto 6px}
.cover .brand-name{font-family:'Comic Neue',cursive;font-weight:700;font-size:24px;color:var(--green-dark);line-height:1}
.cover .brand-tag{font-size:5.8px;color:var(--green-dark);margin-top:3px}
.cover .web{position:absolute;left:0;right:0;top:140px;text-align:center;font-weight:700;font-size:9.6px;line-height:12px;color:var(--green-dark)}
.cover .address{position:absolute;left:0;right:0;top:168px;text-align:center;font-size:5.9px;line-height:8px}
.cover .title-band{position:absolute;left:0;right:0;top:188px;height:79px;background:var(--green-light);color:#fff;text-align:center}
.cover .title-band h1{font-family:'Comic Neue',cursive;font-weight:700;font-size:24px;line-height:23px;padding-top:9px}
.cover .title-band p{font-size:8.6px;margin-top:3px}
.cover .cover-photo{left:0;right:0;top:267px;bottom:5px;background:radial-gradient(ellipse at 55% 55%,#f2e6d8 0%,var(--photo-fur-1) 38%,var(--photo-fur-2) 75%,#2a2520 100%)}

.inside{left:415px;top:96px;width:455px;height:485px}
.inside .col-left{position:absolute;left:12px;top:22px;width:200px}
.inside .col-right{position:absolute;left:235px;top:22px;width:208px}
.inside .heading{font-size:12px;margin-bottom:3px}
.inside .heu{position:absolute;left:12px;top:206px;width:200px}
.inside .heu .heading{font-size:11.5px}
.inside .vitamin{position:absolute;left:118px;top:332px;width:94px}
.inside .kids{position:absolute;left:0;right:0;bottom:0;height:75px;background:var(--green-dark);color:#fff;padding:9px 12px 0}
.inside .kids .heading{display:inline;color:#fff;font-size:12.5px;margin-right:4px}

.outside{left:173px;top:640px;width:687px;height:486px}
.outside .heading{font-size:11px;margin-bottom:3px}
.outside .col-left{position:absolute;left:11px;top:20px;width:205px}
.outside .col-left .heading{margin-bottom:8px}
.outside .col-mid{position:absolute;left:247px;top:148px;width:217px}
.outside .col-mid .heading{margin-top:14px;margin-bottom:7px}
.outside .col-right{position:absolute;left:474px;top:130px;width:201px}
.outside .col-right .heading{margin-bottom:8px}
.outside .quote{position:absolute;left:324px;top:15px;width:136px;font-family:'Comic Neue',cursive;font-weight:700;font-style:italic;font-size:6.4px;line-height:8.2px;color:var(--olive-text)}
.checklist{list-style:none;max-width:128px;text-align:left}
.checklist li{padding-left:4px;text-indent:-4px}
</style>
</head>
<body>

<section class="sheet cover" aria-label="Titelseite">
  <div class="band-top"></div>
  <div class="brand">
    <span class="brand-mark"></span>
    <div class="brand-name">Pfotenkorb-Laden</div>
    <div class="brand-tag">Der Online-Shop für Meerschweinchen, Kaninchen &amp; Co.</div>
  </div>
  <div class="web">www.pfotenkorb-laden.ch<br>info@pfotenkorb-laden.ch</div>
  <div class="address">Pfotenkorb-Laden | Ahornstrasse 7 | 4600 Musterwil<br>Telefon: 061.5550142 | Natel: 078.5550276 | Telefax: 061.5550143</div>
  <div class="title-band">
    <h1>Kleines<br>Meerschweinchen</h1>
    <p>Was man alles über Meerschweinchen wissen sollte.</p>
  </div>
  <div class="photo cover-photo" role="img" aria-label="Foto: Nahaufnahme eines beige-weissen Meerschweinchens im Häuschen"></div>
  <div class="band-bottom"></div>
</section>

<section class="sheet inside" aria-label="Innenseite Ernährung">
  <div class="band-top"></div>

  <div class="info-circle" style="left:106px;top:2px;width:126px;height:126px">
    <svg class="bulb" style="top:7px" width="12" height="14" viewBox="0 0 12 14" aria-hidden="true"><circle cx="6" cy="6" r="3.6" fill="none" stroke="#b8cb4c" stroke-width="1"/><path d="M4.6 9.5h2.8v2.2H4.6z" fill="none" stroke="#b8cb4c" stroke-width=".9"/><path d="M6 0v1M1 2l.8.8M11 2l-.8.8" stroke="#b8cb4c" stroke-width=".8"/></svg>
    <div class="label" style="top:24px">VORSICHT!</div>
    <div class="text" style="top:46px">Meerschweinchen besitzen empfindliche Verdauungsorgane. Es dürfen keine radikalen Futterumstellungen vorgenommen werden. Darauf reagieren sie mit Verdauungsstörungen (Blähungen, Durchfall, Schmerzen). Jeder rasche Futterwechsel ist zu vermeiden und sollte immer über mehrere Tage hinweg erfolgen.</div>
  </div>

  <div class="col-left">
    <div class="wrap-r" style="width:112px;height:112px;shape-outside:circle(69px at 69px 43px)"></div>
    <h2 class="heading">Speisenplan</h2>
    <div class="copy">Meerschweinchen nehmen den ganzen Tag über Nahrung in vielen kleinen Mahlzeiten auf. Etwa 80 Mahlzeiten über den Tag verteilt. Es dürfen keine grossen Pausen zwischen den Mahlzeiten entstehen. Es ist falsch, wenn man ihnen nur einmal am Tag Futter gibt, auch wenn es eine ausreichend grosse Portion ist. Meerschweinchen haben einen Stopfmagen. Das Verdauungssystem ist immer aktiv und durch ständiges Fressen wird die Nahrung im Magen und Darm weiter geschoben. Wenn die Nahrungszufuhr unterbrochen wird, kommt es zu gefährlichen und schmerzhaften Blähungen, weil Lücken entstehen. Es kann bis zu 5 Tage dauern, bis das Futter, das sie aufgenommen haben, wieder ausgeschieden wird. Daher können Fütterungsfehler sehr quälend für die Tiere sein. Es kann zu starken Verdauungsproblemen kommen.</div>
  </div>

  <div class="photo" role="img" aria-label="Foto: zwei Meerschweinchen fressen frisches Grün" style="left:-2px;top:284px;width:114px;height:114px;border-radius:50%;background:radial-gradient(circle at 40% 40%,var(--photo-green-2),var(--photo-green-1) 70%,#1f2614)"></div>

  <div class="heu">
    <div class="hold-l" style="height:76px"></div>
    <div class="wrap-l" style="width:110px;height:84px;shape-outside:circle(63px at 43px 59px)"></div>
    <h2 class="heading">Heu ist das wichtigste Nahrungsmittel!</h2>
    <div class="copy">Es muss, ebenso wie Wasser immer reichlich zur Verfügung stehen! Es enthält wertvolle Rohfaser die für die Verdauung gebraucht wird und dient zum Abrieb der Backenzähne. Die Zähne wachsen ständig nach. Durch das Kauen/Mahlen schleifen sich die Backenzähne ab. Wenn sie das nicht tun, wachsen sie, bis die Seiten in der Mitte zusammenwachsen und eine Brücke bilden. Dann können sie gar nicht mehr fressen und der Tierarzt muss die Zähne abschleifen. Das ist unangenehm und schmerzhaft und bedeutet für die Tiere Stress! Oftmals kommt es dadurch, dass die Meerschweinchen keine Nahrung mehr aufnehmen können auch noch zu Verdauungsstörungen.</div>
  </div>

  <div class="vitamin">
    <h2 class="heading" style="font-size:12px">Vitamin C</h2>
    <div class="copy">Meerschweinchen sind nicht, wie Kaninchen z. B., in der Lage, Vitamin C (Ascorbinsäure) selber zu produzieren. Daher muss man darauf achten, dass sie immer genug Vitamin C durch das Frischfutter</div>
  </div>

  <div class="tag-banner" style="left:10px;top:362px;width:106px;padding:3px 2px;font-size:9px;line-height:10.5px">Achtung GIFTIG:<br>Eibe + Thuja!</div>

  <div class="info-circle" style="left:322px;top:236px;width:128px;height:128px">
    <svg class="bulb" style="top:7px" width="12" height="14" viewBox="0 0 12 14" aria-hidden="true"><circle cx="6" cy="6" r="3.6" fill="none" stroke="#b8cb4c" stroke-width="1"/><path d="M4.6 9.5h2.8v2.2H4.6z" fill="none" stroke="#b8cb4c" stroke-width=".9"/><path d="M6 0v1M1 2l.8.8M11 2l-.8.8" stroke="#b8cb4c" stroke-width=".8"/></svg>
    <div class="label" style="top:24px">NICHT FÜTTERN!</div>
    <div class="text" style="top:45px">Körnerfutter, Johgurtdrops, Knabberstangen und hartes Brot. Sie enthalten zu viel Zucker, der die Verdauung schädigt und Farbstoffe. Leckerlis entsprechen in keiner Weise der natürlichen Ernährung, schaden und verkürzen das Leben! Kopfsalat aus Gewächshäusern (zu hoher Nitrat).</div>
  </div>

  <div class="col-right">
    <div class="hold-r" style="height:208px"></div>
    <div class="wrap-r" style="width:127px;height:142px;shape-outside:circle(70px at 70px 70px)"></div>
    <div class="copy">aufnehmen. Zusätzlich kann man noch Vitamin-C-haltige Pellets ins Trockenfutter mischen. Das ist besonders im Winter wichtig. Wenn Meerschweinchen zu wenig Vitamin C zu sich nehmen, werden sie antriebslos, sitzen apathisch in der Ecke und werden anfällig für Infektionen.</div>
    <h2 class="heading" style="margin-top:7px">Saftfutter</h2>
    <div class="copy">Neben Heu als Grundfutter, das jederzeit zur Verfügung stehen muss, ist der zweite Hauptbestandteil der Ernährung eines Meerschweinchens Saftfutter, also Futter mit hohem Wassergehalt. Idealerweise verfüttert man im Sommer Grünfutter, wie frisch geschnittenes Gras, Löwenzahn, Breit- und Spitzwegerich etc. von nicht gedüngten Wiesen, die nicht an Straßenrändern liegen und nicht von Hunden frequentiert werden. Als Saftfutter eignen sich auch zahlreiche Gemüsearten wie z. B. Salatgurken, Peperoni, Karotten, verschiedene Salatsorten, Fenchel, Stangensellerie, Knollensellerie, Tomaten, Broccoli. Kräuter (Petersilie, Dille, usw.) sind ein beliebter Leckerbissen, sollten aber nur von Zeit zu Zeit in kleineren Mengen verfüttert werden, da sie durch ihren relativ hohen Calcium- und Phosphorgehalt die Bildung von Blasensteinen fördern können (gilt auch für getrocknete Kräuter). Auch einige Obstsorten eignen sich in kleinen Mengen als Saftfutter, z. B. Äpfel, Weintrauben, Melonen. Da die stetig nachwachsenden Zähne durch die Mahlbewegung beim Fressen und Nagen abgenützt werden, ist es wichtig, dass die Tiere auch regelmässig Knabberäste zur Verfügung haben: Obstbäume (Kernobst), Hasel (rot und grün), Weide, Birke, Rottanne, Buche, Eiche sind geeignet. Diese Äste dienen nebst dem Erhalt der Zahngesundheit auch der Beschäftigung.</div>
    <h2 class="heading" style="margin-top:8px">Trockenfutter</h2>
    <div class="copy">Meerschweinchen, die drinnen leben, brauchen nicht unbedingt Trockenfutter und schon gar kein Körnerfutter. Davon werden sie dick und träge. Leider enthält das meiste Futter, das im Handel angeboten wird, sehr viel Getreide. Problematisch am Getreide sind die reifen Getreidekörner, bzw. die darin enthaltene Stärke. Diese Stärke kann im Meerschweinchendarm nur unzureichend aufgespaltet werden und sorgt für ein Ungleichgewicht in der Darmflora. Meerschweinchen, welche bei tiefen Temperaturen im Freien gehalten werden, brauchen deutlich mehr Energie.</div>
  </div>

  <div class="kids">
    <div class="copy"><h2 class="heading">Meerschweinchen und Kinder</h2>Meerschweinchen sind keine Kuscheltiere. Sie eignen sich nicht dazu, von Kindern herumgetragen und geknuddelt zu werden. Da sich Meerschweinchen aufgrund ihres angeborenen Verhaltens nicht wehren können und nur unbeweglich sitzenbleiben, wenn sie Angst haben, wird oft angenommen, dass sie gern durch Kinderhände manipuliert würden. Diese weit verbreitete Meinung ist jedoch falsch und kann unbemerkt zu regelrechten Tierquälereien führen. Wenn Meerschweinchen artgerecht gehalten werden, erfreuen sie uns durch ihr interessantes, natürliches Verhalten. Für jede Tierhaltung gilt: Kinder müssen unbedingt von Erwachsenen angeleitet und beaufsichtigt werden. Sie müssen lernen, mit den ihnen anvertrauten Tieren rücksichtsvoll umzugehen und deren Bedürfnisse zu respektieren.</div>
  </div>
</section>

<section class="sheet outside" aria-label="Aussenseite Haltung">
  <div class="band-top"></div>

  <div class="info-circle" style="left:171px;top:-9px;width:150px;height:150px">
    <svg class="bulb" style="top:12px" width="12" height="14" viewBox="0 0 12 14" aria-hidden="true"><circle cx="6" cy="6" r="3.6" fill="none" stroke="#b8cb4c" stroke-width="1"/><path d="M4.6 9.5h2.8v2.2H4.6z" fill="none" stroke="#b8cb4c" stroke-width=".9"/><path d="M6 0v1M1 2l.8.8M11 2l-.8.8" stroke="#b8cb4c" stroke-width=".8"/></svg>
    <div class="label" style="top:30px">LEBENSRAUM</div>
    <div class="text" style="top:52px;left:8px;right:8px"><b>Drinnen:</b> Für zwei bis drei Meerschweinchen min. 1,5 x 0,75 m in einem Vivarium oder Eigenbau. <b>Draußen:</b> Für drei bis vier Meerschweinchen in 4 m² mit einem zusätzlichem wetterfesten Stall. Beide Gehegevarianten sollten abwechslungsreich gestaltet sein mit mehreren Häuschen, Weidenbrücken, Unterschlüpfen, Grasnestern, Ästen, Zweigen, Wurzeln, Steinen.</div>
  </div>

  <div class="col-left">
    <div class="wrap-r" style="width:51px;height:127px;shape-outside:circle(81px at 81px 46px)"></div>
    <div class="hold-l" style="height:288px"></div>
    <div class="wrap-l" style="width:176px;height:204px;shape-outside:circle(104px at 62px 97px)"></div>
    <h2 class="heading">Wie sieht nun also die artgerechte Haltung von Meerschweinchen aus?</h2>
    <div class="copy">Das Bild von der konventionellen Käfighaltung ist noch viel zu stark in den Köpfen der Menschen verankert. Aber Meerschweinchen sollten nicht in einem Standart-Käfig eingepfercht werden, sondern sie brauchen sehr viel Platz, um in einer Kleingruppe rumwuseln zu können. Die Unterbringung in einem kleinen Käfig stammt noch von früher, als man glaubte, dass man Haustiere zur Belustigung und Unterhaltung/Dekoration in einen Käfig stecken könne. Solche Tiere, die dann gelangweilt und trübsinnig in einem viel zu kleinen Käfig herumhocken, werden sehr schnell uninteressant, die Halter verlieren die Freude an ihnen und die Meerschweinchen werden wieder abgegeben. Seit das Tierschutz-Gesetz am 01. September 2008 in Kraft getreten ist, ist die Einzelhaltung von Meerschweinchen verboten. Meerschweinchen sind Rudeltiere, und sollten nach Möglichkeit in Kleingruppen ab 3-4 Tieren gehalten werden. Sehr oft werden aber immer noch Pärchen gehalten. Zwei Meerschweinchen geben aber kein Rudel ab, hinzu kommt, dass sofort eine Notsituation entsteht, wenn mal ein Tier versterben sollte, dann sitzt das andere alleine im Käfig, und es muss nicht selten in einer Hauruck-Übung ein neues organisiert werden. Bei 3 und mehr Tieren entsteht dieses Problem nie, man kann sich in aller Ruhe Gedanken machen, was für ein Tier zu der Gruppe passen würde. Oft kann man beobachten, dass Tiere, die seit Jahren zu zweit gelebt haben, das Sozialverhalten in einer Gruppe nie gelernt oder verlernt haben. Solche 2-er Meerschweinchen sind dann total auf ihr Gegenüber fixiert. Da ist es dann zum Teil recht schwierig und braucht sehr viel Fingerspitzengefühl und Nerven, um ein drittes oder gleich zwei neue hinzu zu setzen. Aus diesem Grund ist es ratsam, gleich von Anfang an genügend Platz vorzubereiten und als Einstieg mindestens 3 - 4 Tiere zu halten, statt nur 2. Lebensqualität hat für ein Meerschweinchen sehr viel mit dem sozialen Austausch mit Artgenossen zu tun - gerade weil sie Rudeltiere sind. Erst dann wird Meerschweinchenhaltung auch für die Besitzer interessant. Es ist ständig etwas los im Gehege, man kann das Sozialverhalten der Tiere beobachten, denn Meerschweinchen sind nun mal Beobachtungstiere und keine Rum-</div>
  </div>

  <div class="photo" role="img" aria-label="Foto: braunes Meerschweinchen im Einstreu, Nahaufnahme" style="left:-25px;top:307px;width:196px;height:196px;border-radius:50%;background:radial-gradient(circle at 55% 45%,#b07a45,var(--photo-fur-2) 55%,#2b1f16)"></div>
  <div class="tag-banner" style="left:74px;top:438px;width:152px;padding:3px 4px;font-size:10px;transform:rotate(-5deg)">„Ich bin kein Kuscheltier!"</div>

  <p class="quote">„Auf unserer Homepage finden Sie in der Rubrik Meersäulinge zahlreiche Beispiele, wie man Meerschweinchen in Innenhaltung ein artgerechtes Zuhause bieten kann."</p>

  <div class="info-circle" style="left:322px;top:54px;width:146px;height:146px">
    <svg class="bulb" style="top:10px" width="12" height="14" viewBox="0 0 12 14" aria-hidden="true"><circle cx="6" cy="6" r="3.6" fill="none" stroke="#b8cb4c" stroke-width="1"/><path d="M4.6 9.5h2.8v2.2H4.6z" fill="none" stroke="#b8cb4c" stroke-width=".9"/><path d="M6 0v1M1 2l.8.8M11 2l-.8.8" stroke="#b8cb4c" stroke-width=".8"/></svg>
    <div class="label" style="top:28px">FLUCHTTIERE</div>
    <div class="text" style="top:52px;left:7px;right:7px">Bei drohender Gefahr gibt es für Meerschweinchen zwei Möglichkeiten: entweder Angststarre oder Flucht. Daher brauchen sie viele Versteckmöglichkeiten und Unterschlüpfe, in die sie flüchten können, wenn Gefahr droht. Es ist also völlig natürlich, wenn sie in ein Häuschen flüchten, wenn man sie herausgreifen will. Sie müssen das Vertrauen zu den Menschen erst erlernen.</div>
  </div>

  <div class="col-mid">
    <div class="wrap-r" style="width:148px;height:58px;shape-outside:circle(79px at 79px -21px)"></div>
    <div class="copy">trag- und Kuscheltiere! Es wird vielleicht auch mal gezankt und gestritten. Denn auch hier ist das Bild vom träge-trostlos-gelangweilten Meerschweinchen, das dick und antriebslos im Käfig sitzt viel zu verbreitet bei der Bevölkerung. Denn es wird geplappert, gezetert, gewuselt, geklappert, gebrommselt und im Gänsemarsch umhergelaufen etc. Sozialer Austausch, der positive Stress, der Futterneid, die „Diskussionen" und vieles mehr ist für ein gutes Meerschweinchenleben einfach wichtig. Die einfachste und kostengünstigste Variante in Innenhaltung ist der 4-Bretter-Bau: 4 Bretter, die mit Winkeln zusammengeschraubt werden und auf Teichfolie oder ein mit Wachs beschichtetes Tischtuch gestellt werden, und fertig ist der Eigenbau.</div>
    <h2 class="heading">Schutz vor Fressfeinden</h2>
    <div class="copy">Ein wichtiger Aspekt der Aussenhaltung ist der Schutz vor Fressfeinden. Zu diesen gehören nicht nur Fuchs und Vogel, sondern auch Marder, Katzen und Hunde. Man sollte an 3 Punkte denken: drüber, drunter, durch. Das Gehege muss also so abgesichert sein, dass ein Übersteigen bzw. -springen, das Untergraben sowie das Durchdringen nicht möglich ist.<br><b>Geeignete Schutzmassnahmen sind dabei:</b></div>
    <ul class="copy checklist">
      <li>• Zaunmaschengrösse nicht grösser als 1 cm. Passt ein Hühnerei durch die Maschen, passt auch ein Marder oder Wiesel durch.</li>
      <li>• Absicherung von oben durch viereckiges Casanetgitter (sechseckige Hühnerdraht) oder einem festen Dach.</li>
      <li>• Schutz gegen Unter- und Durchgraben: Das komplette Gehege wird auf Gartenplatten gestellt, dies ermöglicht ausserdem eine gute Reinigung des Geheges.</li>
    </ul>
  </div>

  <div class="photo" role="img" aria-label="Foto: Kopf eines braunen Meerschweinchens, seitlich" style="left:474px;top:20px;width:97px;height:97px;background:radial-gradient(circle at 50% 55%,#a8703d,#5a3a22 65%,#2a1d14)"></div>
  <div class="photo" role="img" aria-label="Foto: Meerschweinchen von vorne mit geöffnetem Mäulchen" style="left:578px;top:20px;width:97px;height:97px;background:radial-gradient(circle at 50% 50%,#c48f55,#7a5230 60%,#33251a)"></div>

  <div class="col-right">
    <div class="hold-l" style="height:240px"></div>
    <div class="wrap-l" style="width:30px;height:80px;shape-outside:circle(62px at -33px 60px)"></div>
    <h2 class="heading">Gesundheitskontrolle</h2>
    <div class="copy">Um Krankheiten vorzubeugen und sie schneller zu erkennen, ist es unbedingt notwendig, täglich und wöchentlich eine Gesundheitskontrolle durchzuführen. Täglich beobachtet man seine Meerschweinchen, ob auch alle zu den Futterstellen kommen, wie sie sich verhalten und ob sie wirklich etwas fressen oder nur so tun. Man beobachtet, ob sie entspannt liegen oder gesträubt und apathisch in der Ecke sitzen. Das ist auf jeden Fall ein Zeichen für Unwohlsein und Schmerzen und sollte näher untersucht werden. So beobachtet man das Verhalten und sieht ob alle Meerschweinchen gut drauf sind und mit Elan fressen und sich normal bewegen. Ausserdem sollte man das Gewicht kontrollieren. Eine regelmässige Gewichtskontrolle ist immer eine gute Vorsorge. Optimal ist es, wenn man eine Liste führt mit den Gewichten, so kann man schön vergleichen, und sieht auch, wenn ein Meerschweinchen extrem an Gewicht verliert. Schwankungen bis zu 50g sind im normalen Bereich. Die Tiere sollten wenn möglich zur gleichen Tageszeit gewogen werden. Wenn sie mehr zu- oder abgenommen haben, sollte man sie genauer beobachten bzw. einen Tierarzt zu Rate ziehen. Gründe für Gewichtsabnahmen sind in den meisten Fällen Zahnprobleme. Gleichzeitig werden beim wägen die Krallen kontrolliert, auch wird geschaut, ob die Augen klar sind und keine Verletzungen haben, ob die Ohren sauber, verkrustet oder schuppig sind. Die Nase und das Mäulchen müssen ebenfalls sauber und trocken sein. Ist das Mäulchen gelblich verkrustet, könnte das Lippengrind sein und muss behandelt werden. Und dann wird noch kontrolliert, ob sie speicheln. Auch das kann ein Zeichen für Zahnprobleme sein. Die Vorderzähnchen werden angeschaut, ob sie nicht schief oder zu lang oder abgebrochen sind. Die Backenzähne können nur von einem Tierarzt angeschaut werden. Das sollte man dann machen lassen, wenn sie nicht mehr fressen oder Verdauungsprobleme haben. Dann können Zahnspitzen an den Backenzähnen die Ursache sein und es muss auf jeden Fall schnell etwas dagegen unternommen werden. Bei allen Tieren wird geschaut, ob es kahle Stellen im Fell sind, ob es schuppig ist und ob sichtbare Parasiten vorliegen. Bei kahlen Stellen kann es sich um einen Pilz oder Milbenbefall handeln. Ausserdem werden sie abgetastet, ob die Meerschweinchen irgendwo Wunden oder Beulen haben. Auch am Bauch und unter dem Kiefer (Kieferabszess). Werden Unregelmässigkeiten festgestellt, sollte das Tier einem Tierarzt vorgestellt werden.</div>
  </div>

  <div class="info-circle" style="left:385px;top:374px;width:112px;height:112px">
    <svg class="bulb" style="top:6px" width="12" height="14" viewBox="0 0 12 14" aria-hidden="true"><circle cx="6" cy="6" r="3.6" fill="none" stroke="#b8cb4c" stroke-width="1"/><path d="M4.6 9.5h2.8v2.2H4.6z" fill="none" stroke="#b8cb4c" stroke-width=".9"/><path d="M6 0v1M1 2l.8.8M11 2l-.8.8" stroke="#b8cb4c" stroke-width=".8"/></svg>
    <div class="label" style="top:24px">ALLGEMEIN GILT:</div>
    <div class="text" style="top:45px;left:8px;right:8px">Frisst ein Meerschweinchen nicht, ist dies immer eine Notfallsituation und das Tier muss so schnell wie möglich einem meerschweinchenkundigen Tierarzt vorgestellt werden!.</div>
  </div>

  <div class="band-bottom"></div>
</section>

</body>
</html>
```